New doctor needs elegant, whimsical Business Card Design

CHALLENGE: how to highlight gynaecological service (use of abstract cervix in logo?) in NON-VULGAR way + project an elegant, professional tone?

We need a business card design (incl logo) for a gynaecologist who is starting his private practice. The main area of service will be colposcopy - a diagnostic procedure using a microscope to look at the tissues of the cervix for any potentially cancerous cells.

STYLE: Classic, elegant, timeless look. Fairly simple, not too cluttered. Logo NOT to overpower name. Want to project a professional but approachable image - "gentleman". Not too "corporate" - whimsical, without becoming feminine.

COLOUR: soft colours - no clashing primary colours, nothing too "brash" or commercial.
White background/black lettering + 1 colour accent, pattern repeated throughout card, in both logo & text (refer to "mock-up example" image file)
The colour accent should be BLUE: a serene/calm but confident shade: eg. strong pastel blue, dark baby blue (NOT royal blue, navy, turquoise, aquamarine, etc)

TEXT: have a calligraphy feel (but not too fancy as to be difficult to read at a glance) or more italics/rounded edges kind of font (refer to refer to "mock-up example" image file)
- Contrast between NAME in more italic font Vs. rest of text in "straight" print (or vice versa)

LOGO:
1) something very similar to "The Mira Pledge" logo (ref image attached) - an abstract, black line drawing of a woman's figure, with a single, coloured symbol. No detail in line drawing - NO head or arms - don't want it to be obviously women's figure - want it very stylised, abstract, fluid lines.

* The Mira Pledge used a heart but we would like to use an another symbol in BLUE - maybe an abstract of a cervix? eg. the "triangle" shape symbol (see the image file of the Bright Petal Wellness Initiative - the symbol in the middle of the flower) OR the "donut" representation of the cervix (see notes below)

BUT - don't want the symbol exactly over the groin area, otherwise looks vulgar. Don't want it to look like bikini or genitals! Symbol should be incorporated into line drawing but NOT drawing direct attention to the groin. Maybe displaced to one side? Or further up the body? Open to your ideas

2) We are also open to any other ideas you may have, of stylistic/abstract designs based on:
- the image of a cervix (looks very similar to a pink donut - usually shown in medical shorthand as a tiny circle in the middle of a bigger circle.)
- the cervix with some cells within ? Some stylised version of cancer cells?
(please see attached selection of images for reference/inspiration)

Target Market(s)

2 main audiences: women (18 - 70) concerned about abnormal PAP smear, other gynae-issues, 2) GP's referring their patients to a gynae-specialist

Industry/Entity Type

Medical

Requirements
Must have
• ONE side only - Reverse of business card must be kept blank for "Appointments" notes.

Should not have
• NO "retro" American feel - nor anything 60's or 70's kind of feel. Don't want fonts that look too commercial or industrial/harsh.

Logo: NO obvious silhouettes/profiles of women (abstract is OK but not detail), NO female reproductive system (2 ovaries & uterus), no female symbol - as these are the usual cliches for gynaecologists.

DON'T want the symbol exactly over the groin area, otherwise looks vulgar. Don't want it to look like bikini or genitals! Symbol should be incorporated into line drawing but NOT drawing direct attention to the groin. Maybe displaced to one side? Or further up the body? Open to your ideas

```html
<!DOCTYPE html>
<html lang="en">
<head>
<meta charset="utf-8">
<title>Dr Henry Ashford – Business Card</title>
<link rel="stylesheet" href="https://fonts.googleapis.com/css2?family=Source+Sans+3:ital,wght@0,400;0,600;1,600&display=swap">
<style>
  :root {
    --ink: #000000;
    --accent: #4f93d3;
    --paper: #ffffff;
    --edge: #555555;
  }
  html, body {
    margin: 0;
    padding: 0;
    width: 1200px;
    height: 777px;
    overflow: hidden;
    background: var(--paper);
  }
  .card {
    position: relative;
    width: 1200px;
    height: 777px;
    box-sizing: border-box;
    border: 1.5px solid var(--edge);
    background: var(--paper);
    font-family: "Source Sans 3", "Myriad Pro", sans-serif;
    color: var(--ink);
  }
  .card p { margin: 0; line-height: 1; position: absolute; white-space: nowrap; }

  .brand {
    position: absolute;
    left: 90px;
    top: 230px;
    width: 220px;
    text-align: center;
  }
  .brand__square {
    width: 64px;
    height: 64px;
    margin: 0 auto 22px;
    box-sizing: border-box;
    border: 5px solid var(--ink);
  }
  .brand__name {
    font-size: 30px;
    font-weight: 400;
    line-height: 1.2;
    color: var(--ink);
  }

  .doctor-name {
    left: 410px;
    top: 173px;
    font-size: 76px;
    font-weight: 400;
  }
  .specialty {
    left: 414px;
    top: 283px;
    font-size: 52px;
    font-weight: 600;
    font-style: italic;
    color: var(--accent);
  }
  .credentials {
    left: 414px;
    top: 383px;
    font-size: 28px;
  }

  .address { left: 92px; font-size: 28px; }
  .address--line1 { top: 631px; }
  .address--line2 { top: 673px; }

  .contact { right: 96px; font-size: 28px; text-align: right; }
  .contact__label { display: inline-block; width: 46px; text-align: left; }
  .contact--phone { top: 592px; }
  .contact--fax { top: 631px; }
  .contact--email { top: 673px; color: var(--accent); }
</style>
</head>
<body>
  <div class="card">
    <div class="brand">
      <div class="brand__square"></div>
      <div class="brand__name">Ashford<br>Gynaecology</div>
    </div>

    <p class="doctor-name">Dr Henry Ashford</p>
    <p class="specialty">Gynaecologist</p>
    <p class="credentials">BM,BCh, MA (Oxon), Dip Obs, FRANZCOG, MD</p>

    <p class="address address--line1">Suite 12, Larchwood Medical Centre</p>
    <p class="address address--line2">40 Ferncliff Ave, Westbrook, WA 6100</p>

    <p class="contact contact--phone"><span class="contact__label">T:</span>+61 8 61 00 27 45</p>
    <p class="contact contact--fax"><span class="contact__label">F:</span>+61 8 61 00 27 46</p>
    <p class="contact contact--email">admin@ashfordgyn.com.au</p>
  </div>
</body>
</html>
```